Sleek, Professional Business Card Design Needed

Business Cards - Logo Attached.

We are a solar consulting company. We are national and want our cards to represent the professional high quality products that we offer.

Industry/Entity Type

Business

Contact Information for Business Card

n/a

Requirements
Must have
• Design
• Name
• Position
• Number
• Email
• Address
Should not have
• Not be too crowded

```html
<!DOCTYPE html>
<html lang="en">
<head>
<meta charset="utf-8">
<title>Sunvale Energy – Business Card</title>
<link rel="stylesheet" href="https://fonts.googleapis.com/css2?family=Jost:wght@400;500&family=Roboto:wght@400&display=swap">
<style>
  :root {
    --backdrop: #2b2b2b;
    --card-white: #f1f1f1;
    --brand-blue: #0a8ac8;
    --brand-green: #8dc03f;
    --text-grey: #4a4a4a;
    --white: #ffffff;
  }
  * { margin: 0; padding: 0; box-sizing: border-box; }
  html, body { width: 1200px; height: 960px; overflow: hidden; }
  body { background: var(--backdrop); position: relative; font-family: "Jost", sans-serif; }

  .card { position: absolute; width: 600px; height: 342px; border-radius: 22px; overflow: hidden; }

  .card-front { left: 314px; top: 114px; background: var(--card-white); }
  .edge-strip { position: absolute; left: 0; top: 0; width: 13px; height: 100%; background: var(--brand-blue); }
  .edge-accent { position: absolute; left: 0; top: 51px; width: 13px; height: 50px; background: var(--brand-green); border-top: 2px solid var(--white); border-bottom: 2px solid var(--white); }

  .holder-name { position: absolute; left: 51px; top: 54px; font-size: 21px; font-weight: 500; color: var(--brand-blue); letter-spacing: 0.3px; }
  .holder-title { position: absolute; left: 51px; top: 82px; font-size: 13px; color: var(--brand-green); letter-spacing: 0.6px; }
  .divider { position: absolute; left: 52px; width: 24px; height: 1px; background: var(--brand-green); }
  .divider-top { top: 122px; }
  .divider-bottom { top: 210px; }

  .address { position: absolute; left: 51px; top: 151px; font-size: 14px; line-height: 19px; color: var(--text-grey); }

  .contact-list { position: absolute; left: 52px; top: 238px; list-style: none; }
  .contact-list li { display: flex; align-items: center; height: 20px; font-size: 14px; color: var(--text-grey); }
  .contact-list svg { width: 14px; height: 14px; margin-right: 8px; fill: var(--brand-blue); }

  .brand-front { position: absolute; left: 330px; top: 136px; width: 220px; display: flex; flex-direction: column; align-items: center; }
  .brand-front .brand-circle { width: 70px; height: 70px; border-radius: 50%; border: 6px solid var(--brand-blue); margin-bottom: 20px; }
  .brand-front .brand-name { font-size: 27px; font-weight: 500; color: var(--brand-blue); letter-spacing: 0.5px; white-space: nowrap; }

  .card-back { left: 311px; top: 472px; background: var(--brand-blue); }
  .brand-back { position: absolute; left: 0; top: 140px; width: 100%; text-align: center; font-size: 44px; font-weight: 500; color: var(--white); letter-spacing: 1px; }
  .back-web { position: absolute; left: 0; top: 287px; width: 100%; text-align: center; font-family: "Roboto", sans-serif; font-size: 14px; letter-spacing: 2.4px; color: var(--white); }
</style>
</head>
<body>
  <section class="card card-front">
    <div class="edge-strip"></div>
    <div class="edge-accent"></div>

    <h1 class="holder-name">DANIEL REYES</h1>
    <p class="holder-title">CEO/FOUNDER</p>
    <div class="divider divider-top"></div>

    <p class="address">412 Cedar Ridge Road<br>Fairbanks, Alaska 99701</p>
    <div class="divider divider-bottom"></div>

    <ul class="contact-list">
      <li>
        <svg viewBox="0 0 24 24" aria-hidden="true"><path d="M6.6 10.8a15.1 15.1 0 0 0 6.6 6.6l2.2-2.2c.3-.3.7-.4 1-.2 1.1.4 2.3.6 3.6.6.6 0 1 .4 1 1V20c0 .6-.4 1-1 1A17 17 0 0 1 3 4c0-.6.4-1 1-1h3.5c.6 0 1 .4 1 1 0 1.3.2 2.5.6 3.6.1.3 0 .7-.2 1z"/></svg>
        555 210 4836
      </li>
      <li>
        <svg viewBox="0 0 24 24" aria-hidden="true"><path d="M3 5h18v14H3z M3 5l9 7 9-7" fill="none" stroke="#0a8ac8" stroke-width="2.4"/></svg>
        hello@sunvaleenergy.com
      </li>
      <li>
        <svg viewBox="0 0 24 24" aria-hidden="true"><circle cx="12" cy="12" r="10"/><path d="M7 8c2 0 3 1 3 3s2 1 2 3-1 3-2 4M15 5c0 2 2 2 3 3" fill="none" stroke="#f1f1f1" stroke-width="1.8"/></svg>
        www.sunvaleenergy.com
      </li>
    </ul>

    <div class="brand-front">
      <div class="brand-circle"></div>
      <span class="brand-name">SUNVALE ENERGY</span>
    </div>
  </section>

  <section class="card card-back">
    <p class="brand-back">SUNVALE ENERGY</p>
    <p class="back-web">www.sunvaleenergy.com</p>
  </section>
</body>
</html>
```